Step and Repeat Backdrop for wedding reception photo booth

Would like to have a Step and Repeat Backdrop (8 foot high by 10 foot wide) that incorporates the wedding logo (attached) and the names Elena and Gavin. Background should be white, and wedding colors are burgundy and gold. Show me creativity :-) I have included some random samples.

```html
<!DOCTYPE html>
<html lang="en">
<head>
<meta charset="utf-8">
<title>Elena &amp; Gavin — Step and Repeat Backdrop</title>
<link rel="stylesheet" href="https://fonts.googleapis.com/css2?family=Dancing+Script:wght@700&display=swap">
<style>
  :root {
    --backdrop-grey: #4a4740;
    --frame-tan: #c8bd8c;
    --paper-white: #ffffff;
    --paper-cream: #e7e2cc;
    --gold: #a88a22;
    --gold-light: #e6cf6e;
    --gold-dark: #7a6112;
    --burgundy: #7b1f33;
  }
  * { box-sizing: border-box; margin: 0; padding: 0; }
  html, body {
    width: 1200px;
    height: 1200px;
    overflow: hidden;
    background: var(--backdrop-grey);
  }
  .backdrop {
    position: absolute;
    left: 32px;
    top: 37px;
    width: 1136px;
    height: 907px;
    background: var(--frame-tan);
  }
  .backdrop-field {
    position: absolute;
    left: 25px;
    top: 25px;
    width: 1082px;
    height: 853px;
    background: radial-gradient(ellipse at 50% 50%, var(--paper-white) 35%, #f7f5ea 60%, var(--paper-cream) 100%);
  }
  .name-tile {
    position: absolute;
    width: 290px;
    display: flex;
    flex-direction: column;
    align-items: center;
    gap: 6px;
  }
  .flourish {
    width: 150px;
    height: 34px;
    border-radius: 17px;
    background: linear-gradient(90deg, rgba(168,138,34,0.08), rgba(168,138,34,0.35) 50%, rgba(168,138,34,0.08));
  }
  .name-plaque {
    width: 290px;
    height: 93px;
    border: 3px solid var(--gold);
    box-shadow: inset 0 0 0 1px var(--gold-light), 0 1px 2px rgba(0,0,0,0.25);
    display: flex;
    align-items: center;
    justify-content: center;
  }
  .couple-names {
    font-family: "Dancing Script", cursive;
    font-weight: 700;
    font-size: 44px;
    color: var(--gold);
    white-space: nowrap;
    line-height: 1;
  }
  .wedding-mark {
    position: absolute;
    left: 376px;
    top: 242px;
    width: 347px;
    height: 364px;
    display: flex;
    flex-direction: column;
    align-items: center;
    justify-content: space-between;
  }
  .mark-ornament {
    width: 347px;
    height: 94px;
    border-radius: 47px;
    background: linear-gradient(90deg, rgba(168,138,34,0.08), rgba(168,138,34,0.4) 50%, rgba(168,138,34,0.08));
  }
  .mark-name {
    font-family: "Dancing Script", cursive;
    font-weight: 700;
    font-size: 60px;
    line-height: 1;
    color: var(--burgundy);
    white-space: nowrap;
  }
</style>
</head>
<body>
  <main class="backdrop">
    <section class="backdrop-field">

      <div class="name-tile" style="left:40px; top:58px;">
        <div class="flourish" role="img" aria-label="gold scroll flourish"></div>
        <div class="name-plaque"><span class="couple-names">Elena &amp; Gavin</span></div>
        <div class="flourish" role="img" aria-label="gold scroll flourish"></div>
      </div>
      <div class="name-tile" style="left:402px; top:55px;">
        <div class="flourish" role="img" aria-label="gold scroll flourish"></div>
        <div class="name-plaque"><span class="couple-names">Elena &amp; Gavin</span></div>
        <div class="flourish" role="img" aria-label="gold scroll flourish"></div>
      </div>
      <div class="name-tile" style="left:762px; top:56px;">
        <div class="flourish" role="img" aria-label="gold scroll flourish"></div>
        <div class="name-plaque"><span class="couple-names">Elena &amp; Gavin</span></div>
        <div class="flourish" role="img" aria-label="gold scroll flourish"></div>
      </div>

      <div class="name-tile" style="left:40px; top:264px;">
        <div class="flourish" role="img" aria-label="gold scroll flourish"></div>
        <div class="name-plaque"><span class="couple-names">Elena &amp; Gavin</span></div>
        <div class="flourish" role="img" aria-label="gold scroll flourish"></div>
      </div>
      <div class="name-tile" style="left:762px; top:262px;">
        <div class="flourish" role="img" aria-label="gold scroll flourish"></div>
        <div class="name-plaque"><span class="couple-names">Elena &amp; Gavin</span></div>
        <div class="flourish" role="img" aria-label="gold scroll flourish"></div>
      </div>

      <div class="name-tile" style="left:40px; top:470px;">
        <div class="flourish" role="img" aria-label="gold scroll flourish"></div>
        <div class="name-plaque"><span class="couple-names">Elena &amp; Gavin</span></div>
        <div class="flourish" role="img" aria-label="gold scroll flourish"></div>
      </div>
      <div class="name-tile" style="left:762px; top:468px;">
        <div class="flourish" role="img" aria-label="gold scroll flourish"></div>
        <div class="name-plaque"><span class="couple-names">Elena &amp; Gavin</span></div>
        <div class="flourish" role="img" aria-label="gold scroll flourish"></div>
      </div>

      <div class="name-tile" style="left:40px; top:676px;">
        <div class="flourish" role="img" aria-label="gold scroll flourish"></div>
        <div class="name-plaque"><span class="couple-names">Elena &amp; Gavin</span></div>
        <div class="flourish" role="img" aria-label="gold scroll flourish"></div>
      </div>
      <div class="name-tile" style="left:402px; top:674px;">
        <div class="flourish" role="img" aria-label="gold scroll flourish"></div>
        <div class="name-plaque"><span class="couple-names">Elena &amp; Gavin</span></div>
        <div class="flourish" role="img" aria-label="gold scroll flourish"></div>
      </div>
      <div class="name-tile" style="left:762px; top:674px;">
        <div class="flourish" role="img" aria-label="gold scroll flourish"></div>
        <div class="name-plaque"><span class="couple-names">Elena &amp; Gavin</span></div>
        <div class="flourish" role="img" aria-label="gold scroll flourish"></div>
      </div>

      <div class="wedding-mark">
        <div class="mark-ornament" role="img" aria-label="gold scroll ornament above the wedding logo"></div>
        <span class="mark-name">Elena &amp; Gavin</span>
        <div class="mark-ornament" role="img" aria-label="gold scroll ornament below the wedding logo"></div>
      </div>

    </section>
  </main>
</body>
</html>
```